exclusive Speakeasy Bar Web design in New Jersey USA

We are opening a speakeasy in New Jersey USA soon. we are looking for a web designer to do our web site including the coding. we a looking for a 4 to 5 page web design. the site will be mostly static. home page, contact page, menu page and a link to a 3rd party site (most likely Quob) for reservations. we are looking for this designer to do our menu deign as well. we are looking for a quick turnaround 7-10 days. i am attaching some pictures for the designers to see the concept design and the actual current pictures with our logo as well. professionally taken pictures will be provided later on. our photographer will be taking the pictures in the next week.

Industry/Entity Type

Restaurant, Bar, Speakeasy

Coding

Coded - Design and coding required

Number of Pages Required

4 page

Requirements
Must have
• home page, contact page, menu page and a link to quob.com for reservations
Nice to have
• some videos

```html
<!DOCTYPE html>
<html lang="en">
<head>
<meta charset="utf-8">
<title>Ledger Social</title>
<link rel="stylesheet" href="https://fonts.googleapis.com/css2?family=Poppins:wght@400;500&family=Libre+Baskerville&display=swap">
<style>
  :root{
    --gold:#b8924a;
    --gold-light:#c9a35c;
    --ink:#1b1b1b;
    --white:#ffffff;
    --footer-bg:#ffffff;
  }
  *{margin:0;padding:0;box-sizing:border-box}
  html,body{width:1200px;height:713px;overflow:hidden;background:var(--footer-bg)}
  body{position:relative;font-family:'Poppins',sans-serif;color:var(--white)}
  .hero{position:absolute;left:0;top:0;width:1200px;height:675px;overflow:hidden}
  .hero-photo{position:absolute;inset:0;
    background:
      radial-gradient(ellipse 30% 35% at 50% 30%, rgba(170,110,50,.55), transparent 70%),
      radial-gradient(ellipse 25% 30% at 90% 30%, rgba(150,100,50,.45), transparent 70%),
      radial-gradient(ellipse 25% 30% at 10% 30%, rgba(150,90,50,.45), transparent 70%),
      radial-gradient(ellipse 60% 25% at 50% 70%, rgba(120,70,40,.5), transparent 70%),
      linear-gradient(180deg,#1a1614 0%,#3a2a1e 30%,#2c2018 60%,#45403c 88%,#3a3634 100%)}
  .hero-shade{position:absolute;inset:0;background:rgba(10,8,6,.35)}
  .rule{position:absolute;left:0;width:1200px;height:2px;background:var(--gold)}
  .rule.top{top:30px}.rule.bottom{top:105px}
  .nav{position:absolute;top:59px;font-size:13.5px;letter-spacing:.2px}
  .nav a{position:absolute;white-space:nowrap;color:var(--white);text-decoration:none}
  .nav a.active{color:var(--gold-light)}
  .brand{position:absolute;left:558px;top:12px;width:84px;height:112px;background:#16130f;
    display:flex;flex-direction:column;align-items:center;justify-content:center;
    font-family:'Poppins',sans-serif;font-weight:500;font-size:13px;line-height:1.3;letter-spacing:1.5px;color:var(--white);text-align:center}
  .social{position:absolute;top:53px;width:30px;height:30px;border-radius:50%;border:1.5px solid var(--white)}
  .social.filled{background:var(--gold);border-color:var(--gold)}
  .headline{position:absolute;left:0;top:268px;width:1200px;text-align:center;
    font-family:'Libre Baskerville',serif;font-size:40px;line-height:50px;color:var(--white)}
  .lede{position:absolute;left:280px;top:383px;width:640px;text-align:center;font-size:13.5px;line-height:22.5px}
  .menu-btn{position:absolute;left:520px;top:464px;width:159px;height:37px;border:1.5px solid var(--gold);
    color:var(--gold-light);font-size:13.5px;display:flex;align-items:center;justify-content:center}
  .menu-btn-frame{position:absolute;left:0;top:0}
  .progress{position:absolute;left:0;top:673px;width:435px;height:2px;background:var(--gold)}
  .pager{position:absolute;left:982px;top:619px;width:218px;height:56px;background:var(--white);color:var(--ink);font-size:12px}
  .pager .prev{position:absolute;left:21px;top:19px;color:var(--gold);display:flex;align-items:center;gap:10px}
  .pager .next{position:absolute;right:16px;top:19px;display:flex;align-items:center;gap:8px}
  .footer{position:absolute;left:0;top:684px;width:1200px;text-align:center;font-size:13px;color:var(--ink)}
</style>
</head>
<body>
  <section class="hero">
    <div class="hero-photo" role="img" aria-label="Photo of a backlit bar shelf lined with liquor bottles and glassware"></div>
    <div class="hero-shade"></div>
    <div class="rule top"></div>
    <div class="rule bottom"></div>

    <nav class="nav">
      <a class="active" style="left:103px">HOME</a>
      <a style="left:241px">MENU</a>
      <a style="left:368px">CONTACT US</a>
    </nav>

    <div class="brand">LEDGER<br>SOCIAL</div>

    <a class="social filled" style="left:1036px" aria-label="Social link 1"></a>
    <a class="social" style="left:1073px" aria-label="Social link 2"></a>
    <a class="social" style="left:1109px" aria-label="Social link 3"></a>

    <h1 class="headline">Click here to make a RESERVATION on<br>quob.com</h1>
    <p class="lede">Lorem Ipsum is simply dummy text of the printing and typesetting industry. Lorem Ipsum has been the industry's standard dummy text ever since the 1500s, when an unknown printer</p>

    <svg class="menu-btn-frame" width="1200" height="713" viewBox="0 0 1200 713" aria-hidden="true">
      <g fill="none" stroke="#b8924a" stroke-width="1.5">
        <polyline points="517,459 517,470"/>
        <polyline points="517,459 522,459"/>
        <rect x="513" y="455" width="8" height="8"/>
        <rect x="679" y="502" width="8" height="8"/>
      </g>
    </svg>
    <a class="menu-btn">View Our Menu</a>

    <div class="progress"></div>

    <div class="pager">
      <span class="prev">
        <svg width="23" height="10" viewBox="0 0 23 10"><path d="M23 5H2M6 1 2 5l4 4" fill="none" stroke="#b8924a" stroke-width="1.6"/></svg>
        Preview
      </span>
      <span class="next">
        Next
        <svg width="23" height="10" viewBox="0 0 23 10"><path d="M0 5h21M17 1l4 4-4 4" fill="none" stroke="#1b1b1b" stroke-width="1.6"/></svg>
      </span>
    </div>
  </section>

  <footer class="footer">© 2023&nbsp; LEDGER SOCIAL. All Right Reserved.</footer>
</body>
</html>
```